Polystyrene Environmental Synopsis

We need a fact sheet for quick reference that groups information units and has a simple but engaging visual presentation of the text and various infographics. We are a trade association representing polystyrene foam manufacturers and this piece is intended to help our members provide effective messaging to their sales personnel.

To view our typical company design/style please see our website at www.kvrtradegroup.org. Our primary RGB colors are: (187,140,9); (94,47,29); (94,138,164); and (164,167,15). Secondary RGB colors are (249,162,28) and (218,210,208). Our title/header font is DIN Next LT Pro and our copy font is Calibri 10.5 pt. We can deviate from the font specification if beneficial.

Target Market(s)

Polystyrene manufacturer plant workers and other employees.

Font styles to use
Sans Serif

Requirements
Must have
• Information presentation must be clean and easy to reference.

```html
<!DOCTYPE html>
<html lang="en">
<head>
<meta charset="utf-8">
<title>EPS Talking Points – Polystyrene Defense Line</title>
<link href="https://fonts.googleapis.com/css2?family=Barlow+Semi+Condensed:wght@500;600;700&family=Carlito:wght@400;700&display=swap" rel="stylesheet">
<style>
  :root {
    --gold: rgb(187,140,9);
    --brown: rgb(94,47,29);
    --olive: rgb(164,167,15);
    --olive-pale: rgb(226,228,170);
    --ink: #2a211c;
    --rule: rgb(218,210,208);
    --white: #ffffff;
  }
  * { margin: 0; padding: 0; box-sizing: border-box; }
  html, body { width: 1200px; height: 858px; overflow: hidden; background: var(--white); }
  .sheet { position: relative; width: 1200px; height: 858px; overflow: hidden; background: var(--white); font-family: "Carlito", "Calibri", sans-serif; color: var(--ink); }

  .masthead-band { position: absolute; left: 0; top: 0; width: 1200px; height: 116px; background: var(--brown); }
  .masthead-badge { position: absolute; left: 0; top: 0; width: 410px; height: 138px; background: var(--gold); border-bottom-right-radius: 34px; }
  .badge-eps { position: absolute; left: 22px; top: 14px; font-family: "Barlow Semi Condensed", sans-serif; font-weight: 600; font-size: 96px; line-height: 1; color: var(--white); letter-spacing: 1px; }
  .badge-divider { position: absolute; left: 190px; top: 22px; width: 4px; height: 94px; background: var(--white); }
  .badge-title { position: absolute; left: 208px; top: 24px; font-family: "Barlow Semi Condensed", sans-serif; font-weight: 500; font-size: 44px; line-height: 44px; color: var(--brown); }
  .masthead-intro { position: absolute; left: 428px; top: 20px; width: 760px; font-size: 17.5px; line-height: 23px; color: var(--white); }

  .section-band { position: absolute; left: 0; top: 180px; width: 1200px; height: 60px; background: var(--olive); }
  .section-band-pale { position: absolute; left: 410px; top: 200px; width: 790px; height: 40px; background: var(--olive-pale); }
  .section-title { position: absolute; right: 22px; top: 199px; font-family: "Barlow Semi Condensed", sans-serif; font-weight: 700; font-size: 32px; line-height: 42px; color: var(--olive); letter-spacing: 0.5px; }

  .tab { position: absolute; left: 0; width: 356px; background: var(--brown); border-top-right-radius: 26px; }
  .tab::after { content: ""; position: absolute; left: 0; bottom: -14px; width: 356px; height: 14px; background: var(--gold); }
  .tab-label { position: absolute; right: 22px; text-align: right; font-family: "Barlow Semi Condensed", sans-serif; font-weight: 500; font-size: 38px; line-height: 46px; color: var(--white); }
  .tab-point { top: 284px; height: 300px; }
  .tab-point .tab-label { top: 66px; }
  .tab-voice { top: 636px; height: 180px; }
  .tab-voice .tab-label { top: 22px; }

  .column-rule { position: absolute; left: 360px; top: 284px; width: 2px; height: 544px; background: var(--rule); }

  .copy { position: absolute; left: 408px; width: 766px; font-size: 18px; line-height: 22.5px; }
  .copy-point { top: 302px; }
  .copy-voice { top: 688px; }
</style>
</head>
<body>
<main class="sheet">
  <header>
    <div class="masthead-band"></div>
    <div class="masthead-badge">
      <span class="badge-eps">EPS</span>
      <span class="badge-divider"></span>
      <span class="badge-title">Talking<br>Points</span>
    </div>
    <p class="masthead-intro">Polystyrene bans, recycling, and human health are top objections facing the EPS industry. When confronted with false allegations about EPS, here are some fast facts to help respond proactively. Perfect for packaging conferences, social media, and sales objectives.</p>
  </header>

  <div class="section-band"></div>
  <div class="section-band-pale"></div>
  <h1 class="section-title">POLYSTYRENE DEFENSE LINE</h1>

  <div class="column-rule"></div>

  <section>
    <div class="tab tab-point"><h2 class="tab-label">MAKING<br>YOUR<br>POINT</h2></div>
    <p class="copy copy-point">Speaking with confidence means knowing your material. When responding to misstatements be prepared to challenge the source with factual information. Using a question format is less confrontational, e.g., “Did you know…” or “Were you aware…”? Make affirmative statements whenever possible; avoid restating the misinformation in your response. When addressing someone that refuses to give reasonable consideration to new information, we recommend responding, “It’s unfortunate you’re not willing to look into this further.”<br>When given the opportunity to address an individual or an audience about EPS sustainability, focus on three (3) specific talking points to keep the discussion or presentation focused. Plan your talking points and don’t deviate; this is an effective strategy for dealing with media inquiries as well.</p>
  </section>

  <section>
    <div class="tab tab-voice"><h2 class="tab-label">HAVE A<br>BIGGER<br>VOICE</h2></div>
    <p class="copy copy-voice">The more educated we are, the more educated others will be. Share this document with your employees even if they do not deal directly with your customers or specific packaging audiences. Everyone working within the EPS industry should be aware of the strong environmental profile for EPS.</p>
  </section>
</main>
</body>
</html>
```